Award winning pet photographer needs business card and letterhead

Business card and letterhead for our Pet photography business. We specialize in studio portraits of dogs.

Target Market(s)

Wealthy and middle class dog owners who would like photos of their dogs as wall art.

Industry/Entity Type

Portrait Photography

Contact Information for Business Card

Our business name is Tails of Glee Pet Photography. Would be good to include dog and a heart, bright colours and a modern design

Font styles to use
Sans Serif

Colors
f04a50
f68d4d
faa54b
33a6d7
33b8a4
abd036

Requirements
Must have
• Business name: Tails of Glee Pet Photography
• Phone number: 0497 560314
• Email: marcus@kwstudio.com.au
• Website:www.tailsofglee.com.au
• Photographer: Marcus Holloway
Nice to have
• In Addition letterhead should include
• Studio address 27 Fennick Court, Leederville 6007
• Postal Address 8 Ormsby Ave, West Leederville 6007

```html
<!DOCTYPE html>
<html lang="en">
<head>
<meta charset="utf-8">
<title>Tails of Glee Pet Photography – Business Card</title>
<link rel="stylesheet" href="https://fonts.googleapis.com/css2?family=Montserrat:wght@400;500&family=Oswald:wght@500;700&display=swap">
<style>
  :root {
    --backdrop: #ece8e3;
    --card-white: #ffffff;
    --teal: #33b8a4;
    --teal-deep: #2aa892;
    --teal-text: #2fae9a;
    --grey-text: #5f8f88;
    --lime: #abd036;
    --coral: #f04a50;
    --sun: #faa54b;
    --fur-light: #f6ead6;
    --fur-mid: #e2c79d;
  }
  * { box-sizing: border-box; margin: 0; padding: 0; }
  html, body {
    width: 1200px;
    height: 802px;
    overflow: hidden;
    background: var(--backdrop);
  }
  .canvas {
    position: relative;
    width: 1200px;
    height: 802px;
    display: flex;
    align-items: center;
    justify-content: center;
    gap: 90px;
  }
  .card {
    position: relative;
    width: 390px;
    height: 640px;
    box-shadow: 0 10px 28px rgba(0, 0, 0, 0.18);
    overflow: hidden;
  }

  /* Back side: contact details */
  .card-back {
    background: var(--card-white);
    font-family: "Montserrat", sans-serif;
  }
  .contact {
    position: absolute;
    right: 48px;
    top: 250px;
    text-align: right;
    color: var(--teal-text);
  }
  .contact-name {
    font-size: 19px;
    font-weight: 500;
    letter-spacing: 0.08em;
    text-transform: uppercase;
  }
  .contact-role {
    font-size: 12px;
    font-weight: 500;
    letter-spacing: 0.16em;
    text-transform: uppercase;
    color: var(--grey-text);
    margin-top: 3px;
  }
  .contact-lines {
    list-style: none;
    margin-top: 22px;
    font-size: 14px;
    line-height: 1.45;
    letter-spacing: 0.02em;
  }
  .studio-mark {
    position: absolute;
    left: 40px;
    bottom: 48px;
    display: flex;
    align-items: center;
    gap: 8px;
  }
  .studio-mark-square {
    width: 12px;
    height: 12px;
    background: var(--lime);
  }
  .studio-mark-name {
    font-family: "Montserrat", sans-serif;
    font-weight: 500;
    font-size: 11px;
    letter-spacing: 0.04em;
    color: var(--lime);
    white-space: nowrap;
  }

  /* Front side: brand */
  .card-front {
    background: var(--teal);
  }
  .paw-pattern {
    position: absolute;
    inset: 0;
    background: linear-gradient(160deg, var(--teal) 0%, var(--teal-deep) 100%);
  }
  .brand {
    position: absolute;
    left: 52px;
    top: 58px;
  }
  .brand-name {
    font-family: "Oswald", sans-serif;
    font-weight: 700;
    font-size: 50px;
    line-height: 0.98;
    color: #ffffff;
  }
  .brand-place {
    margin-top: 12px;
    font-family: "Oswald", sans-serif;
    font-weight: 500;
    font-size: 13px;
    letter-spacing: 0.14em;
    text-transform: uppercase;
    color: var(--sun);
    white-space: nowrap;
  }
  .heart-art {
    position: absolute;
    inset: 0;
  }
</style>
</head>
<body>
<main class="canvas">

  <section class="card card-back" aria-label="Business card back">
    <div class="contact">
      <h1 class="contact-name">Marcus Holloway</h1>
      <p class="contact-role">Photographer</p>
      <ul class="contact-lines">
        <li>0497 560314</li>
        <li>marcus@kwstudio.com.au</li>
        <li>www.tailsofglee.com.au</li>
      </ul>
    </div>
    <div class="studio-mark">
      <span class="studio-mark-square"></span>
      <span class="studio-mark-name">Kestrel Works Studio</span>
    </div>
  </section>

  <section class="card card-front" aria-label="Business card front">
    <div class="paw-pattern" role="img" aria-label="Scattered paw print pattern in darker teal"></div>
    <div class="brand">
      <h2 class="brand-name">Tails of<br>Glee<br>Photography</h2>
      <p class="brand-place">Larkwood Vale Sunward Coast</p>
    </div>
    <svg class="heart-art" viewBox="0 0 390 640" width="390" height="640">
      <path class="ribbon" d="M82 440 L262 440 L278 640 L70 640 Z" fill="var(--coral)"/>
      <path class="heart-frame"
            d="M0,-30 C-10,-55 -50,-55 -50,-20 C-50,10 -15,30 0,50 C15,30 50,10 50,-20 C50,-55 10,-55 0,-30Z"
            transform="translate(172 410) scale(2.15)" fill="#ffffff"/>
      <defs>
        <radialGradient id="fur" cx="0.45" cy="0.55" r="0.6">
          <stop offset="0" stop-color="var(--fur-light)"/>
          <stop offset="1" stop-color="var(--fur-mid)"/>
        </radialGradient>
      </defs>
      <path class="heart-photo" role="img" aria-label="Photo of a happy golden retriever puppy"
            d="M0,-30 C-10,-55 -50,-55 -50,-20 C-50,10 -15,30 0,50 C15,30 50,10 50,-20 C50,-55 10,-55 0,-30Z"
            transform="translate(172 414) scale(1.85)" fill="url(#fur)"/>
    </svg>
  </section>

</main>
</body>
</html>
```